Flyer for cleaning services with special cut and space for general awareness

We need one flyer for cleaning services marketing. Its 2 page flyer preferred to have a special design [attracting people] . Colours should be from our brand guidelines.
We need a space in the flyer to paste one small ' hand wipes' with a general awareness of cleanliness.This flyer can be DL size . But we prefer to have a special design cut which attract people
Our services are
Office /Residential cleaning services
Deep cleaning
Move in /Move out
Carpet shampooing
Villa general cleaning
Apartment general cleaning
Event cleaning

Target Market(s)

Dubai

Industry/Entity Type

Cleaning Service

Font styles to use
Serif
Sans Serif

Requirements
Must have
• Brand guideline colours ,our staff photos
Nice to have
• Special design. cut [for Eg: shape of some cleaning equip]

```html
<!DOCTYPE html>
<html lang="en">
<head>
<meta charset="utf-8">
<title>Gulfline Facilities – Cleaning Service Flyers</title>
<link rel="stylesheet" href="https://fonts.googleapis.com/css2?family=Montserrat:wght@400;500;700;800;900&family=Open+Sans:wght@400;600;700&display=swap">
<style>
  :root{
    --navy:#1e1c4f;
    --sky:#29a8e0;
    --yellow:#ffd200;
    --aqua:#a9dde4;
    --teal:#3fb0c2;
    --red:#e8242b;
    --ink:#222233;
    --paper:#ffffff;
    --backdrop:#3b3b3d;
  }
  *{box-sizing:border-box;margin:0;padding:0}
  html,body{width:1080px;height:1200px;overflow:hidden}
  body{background:var(--backdrop);position:relative;font-family:"Montserrat",sans-serif;color:var(--ink)}
  .flyer{position:absolute;background:var(--paper);overflow:hidden}
  .flyer--services{left:55px;top:117px;width:471px;height:999px}
  .flyer--hygiene{left:549px;top:109px;width:474px;height:1007px}
  .abs{position:absolute}

  .brand{display:flex;align-items:center;gap:8px;font-family:"Montserrat",sans-serif;font-weight:700;color:var(--navy);font-size:19px;letter-spacing:-.2px}
  .brand__mark{width:18px;height:18px;background:var(--sky)}
  .flyer--services .brand{left:0;right:0;top:40px;justify-content:center}
  .flyer--hygiene .brand{right:28px;top:42px;font-size:17px}

  .photo{position:absolute}
  .photo--team{background:linear-gradient(180deg,#f3f5f8 0%,#c9d2e2 45%,#2a2d5e 100%);border-radius:48% 48% 6px 6px / 30% 30% 6px 6px}
  .photo--circle{border-radius:50%;border:4px solid var(--yellow);background:radial-gradient(circle at 40% 35%,#e9eef3 0%,#9aa6bd 55%,#2b2f63 100%)}

  .badge{position:absolute}
  .badge svg{position:absolute;inset:0;width:100%;height:100%}
  .badge__text{position:absolute;left:0;right:0;text-align:center;font-weight:800;line-height:.95;transform:rotate(-6deg)}
  .badge__text .w1{display:block;color:#fff}
  .badge__text .w2{display:block;color:var(--yellow)}

  .heading{position:absolute;left:0;right:0;text-align:center}
  .heading__lead{color:var(--sky);font-weight:700;font-size:29px;line-height:1.1}
  .heading__sub{color:var(--navy);font-weight:400;font-size:29px;line-height:1.2}

  .services{position:absolute;left:30px;top:650px;width:430px;display:grid;grid-template-columns:212px 218px;row-gap:10px;list-style:none}
  .services li{display:flex;gap:10px;font-size:17px;color:var(--navy);line-height:1.25}
  .services svg{flex:none;width:18px;height:18px;margin-top:2px}

  .band{position:absolute;left:0;right:0;background:var(--sky)}
  .contact{position:absolute;left:0;right:0;bottom:0;background:var(--navy);color:#fff;font-family:"Open Sans",sans-serif;text-align:center}
  .contact__title{font-weight:600;font-size:16px;letter-spacing:.5px;padding-top:17px}
  .contact__lines{display:flex;justify-content:center;gap:24px;margin-top:8px;font-weight:700;font-size:27px}
  .contact__item{display:flex;align-items:center;gap:10px}
  .dot{width:18px;height:18px;border-radius:50%;border:2.5px solid #fff}

  .aware{position:absolute;left:0;right:0;top:428px;height:484px;background:var(--aqua)}
  .aware__title{position:absolute;left:0;right:0;top:18px;text-align:center;color:var(--red);font-weight:900;font-size:44px;line-height:1.12;letter-spacing:-1.2px}
  .aware__intro{position:absolute;left:0;right:0;top:128px;text-align:center;font-size:11.5px;line-height:1.35;color:#222}
  .aware__intro b{font-weight:700}
  .aware__divider{position:absolute;left:236px;top:212px;width:1px;height:266px;background:#7cc7d3}
  .aware__icon{position:absolute;top:216px;height:100px;border-radius:12px;background:linear-gradient(180deg,#bfe6eb,#94d1db)}
  .method{position:absolute;top:338px;color:var(--teal);font-weight:900;font-size:19px;letter-spacing:-.3px;text-align:center;width:200px}
  .steps{position:absolute;top:371px;list-style:none;font-size:10px;line-height:15.7px;color:#1b1b1b}
  .steps li{display:flex;align-items:center;gap:7px}
  .steps i{font-style:normal;width:9px;height:9px;border-radius:50%;background:var(--red);color:#fff;font-size:6.5px;font-weight:700;display:flex;align-items:center;justify-content:center}
  .partner{position:absolute;left:270px;top:436px;width:130px;height:28px;border-radius:14px;background:#8fcbd5}
</style>
</head>
<body>

<section class="flyer flyer--services">
  <div class="brand abs"><span class="brand__mark"></span>Gulfline Facilities</div>

  <div class="photo photo--team" style="left:20px;top:100px;width:425px;height:290px" role="img" aria-label="Photo of three smiling cleaning staff in navy uniforms holding cleaning supplies"></div>

  <div class="badge" style="left:14px;top:372px;width:440px;height:168px">
    <svg viewBox="0 0 440 168" preserveAspectRatio="none" aria-hidden="true">
      <path fill="#1e1c4f" d="M18 70 L60 46 L120 38 L190 22 L260 14 L330 8 L400 4 L432 20 L424 50 L438 72 L420 96 L428 118 L396 134 L340 140 L290 152 L230 162 L170 160 L110 150 L60 140 L10 130 L22 108 L4 92 Z"/>
    </svg>
    <div class="badge__text" style="top:38px;font-size:46px"><span class="w1">CLEANING</span><span class="w2">SERVICE</span></div>
  </div>

  <div class="heading" style="top:570px">
    <div class="heading__lead">Office &amp; Residential</div>
    <div class="heading__sub">Cleaning Services</div>
  </div>

  <ul class="services">
    <li><svg viewBox="0 0 20 20"><path d="M2 11 L8 16 L18 4" fill="none" stroke="#ffd200" stroke-width="4" stroke-linecap="round" stroke-linejoin="round"/></svg>Deep cleaning</li>
    <li><svg viewBox="0 0 20 20"><path d="M2 11 L8 16 L18 4" fill="none" stroke="#ffd200" stroke-width="4" stroke-linecap="round" stroke-linejoin="round"/></svg>Villa general cleaning</li>
    <li><svg viewBox="0 0 20 20"><path d="M2 11 L8 16 L18 4" fill="none" stroke="#ffd200" stroke-width="4" stroke-linecap="round" stroke-linejoin="round"/></svg>Move in /Move out</li>
    <li><svg viewBox="0 0 20 20"><path d="M2 11 L8 16 L18 4" fill="none" stroke="#ffd200" stroke-width="4" stroke-linecap="round" stroke-linejoin="round"/></svg>Event cleaning</li>
    <li><svg viewBox="0 0 20 20"><path d="M2 11 L8 16 L18 4" fill="none" stroke="#ffd200" stroke-width="4" stroke-linecap="round" stroke-linejoin="round"/></svg>Carpet shampooing</li>
    <li><svg viewBox="0 0 20 20"><path d="M2 11 L8 16 L18 4" fill="none" stroke="#ffd200" stroke-width="4" stroke-linecap="round" stroke-linejoin="round"/></svg>Apartment general cleaning</li>
  </ul>

  <div class="band" style="top:840px;height:64px"></div>
  <div class="photo photo--circle" style="left:30px;top:776px;width:118px;height:118px" role="img" aria-label="Staff member spraying and wiping a window"></div>
  <div class="photo photo--circle" style="left:174px;top:776px;width:118px;height:118px" role="img" aria-label="Staff member wiping a glass door with a blue cloth"></div>
  <div class="photo photo--circle" style="left:320px;top:776px;width:118px;height:118px" role="img" aria-label="Staff member dusting an office chair with a feather duster"></div>

  <footer class="contact" style="height:95px">
    <div class="contact__title">CONTACT US</div>
    <div class="contact__lines">
      <span class="contact__item"><span class="dot"></span>050 318 4726</span>
      <span class="contact__item"><svg width="22" height="22" viewBox="0 0 24 24"><path d="M6 3 L10 7 L7.5 10 Q10 15 14 16.5 L17 14 L21 18 L18 21 Q8 20 3 6 Z" fill="#ffd200"/></svg>04 557 0193</span>
    </div>
  </footer>
</section>

<section class="flyer flyer--hygiene">
  <div class="brand abs"><span class="brand__mark"></span>Gulfline Facilities</div>

  <div class="photo photo--circle" style="left:109px;top:22px;width:120px;height:120px" role="img" aria-label="Staff member spraying and wiping a window"></div>
  <div class="photo photo--circle" style="left:19px;top:126px;width:120px;height:120px" role="img" aria-label="Staff member wiping a glass door"></div>
  <div class="photo photo--circle" style="left:31px;top:280px;width:106px;height:106px" role="img" aria-label="Staff member dusting an office chair"></div>

  <div class="photo photo--team" style="left:166px;top:130px;width:268px;height:180px" role="img" aria-label="Photo of three cleaning staff in navy uniforms with cleaning supplies"></div>

  <div class="badge" style="left:161px;top:294px;width:274px;height:114px">
    <svg viewBox="0 0 274 114" preserveAspectRatio="none" aria-hidden="true">
      <path fill="#29a8e0" d="M10 50 L40 26 L90 18 L140 10 L190 4 L240 2 L268 14 L262 36 L272 56 L256 78 L262 96 L220 102 L170 108 L120 112 L70 110 L30 104 L2 96 L14 78 L0 64 Z"/>
    </svg>
    <div class="badge__text" style="top:26px;font-size:30px"><span class="w1">CLEANING</span><span class="w2">SERVICE</span></div>
  </div>

  <div class="aware">
    <div class="aware__title">A clean hand is<br>a caring hand.</div>
    <div class="aware__intro"><b>Did you know proper hand hygiene is the<br>#1 way to prevent the spread of germs?</b><br>Follow these simple steps for proper hand hygiene.</div>
    <div class="aware__divider"></div>
    <div class="aware__icon" style="left:63px;width:137px" role="img" aria-label="Line illustration of hands washing with soap bubbles"></div>
    <div class="aware__icon" style="left:287px;width:108px" role="img" aria-label="Line illustration of a hand under a sanitizer pump bottle"></div>

    <div class="method" style="left:26px">Soap and water</div>
    <div class="method" style="left:251px">Hand sanitizer</div>

    <ol class="steps" style="left:36px">
      <li><i>1</i>Turn on water</li>
      <li><i>2</i>Wet hands</li>
      <li><i>3</i>Apply soap to palm of one hand</li>
      <li><i>4</i>Scrub for 15 seconds</li>
      <li><i>5</i>Rinse</li>
      <li><i>6</i>Dry with paper towel</li>
      <li><i>7</i>Turn off water with a clean towel</li>
    </ol>
    <ol class="steps" style="left:256px">
      <li><i>1</i>Apply to palm of one hand</li>
      <li><i>2</i>Rub over both hands</li>
      <li><i>3</i>Let dry</li>
    </ol>
    <div class="partner" role="img" aria-label="Partner badge"></div>
  </div>

  <footer class="contact" style="height:95px">
    <div class="contact__title">CONTACT US</div>
    <div class="contact__lines">
      <span class="contact__item"><span class="dot"></span>050 318 4726</span>
      <span class="contact__item"><svg width="22" height="22" viewBox="0 0 24 24"><path d="M6 3 L10 7 L7.5 10 Q10 15 14 16.5 L17 14 L21 18 L18 21 Q8 20 3 6 Z" fill="#ffd200"/></svg>04 557 0193</span>
    </div>
  </footer>
</section>

</body>
</html>
```